RW Stewardship real estate management company needs presentation folder to hand clients

looking for a folder with pockets that represent my real estate management company when i hand to client reports or promotional material. I only do resedential real estate. I want classy and professional - pictures or additioal graphixs are fine

when a client open i will usally insert text and reports about my business
also on the inside flap is usally place for my business card i will upload a picture so the theme can be constant

Target Market(s)

my existing real estate cleints
and i will use when i am soliciting new business

Industry/Entity Type

Real Estate

Font styles to use
Serif

Requirements
Must have
• must have logo
• must give appearance of professionalism and maturity
• have basic company info tel# ,address
• id like viewer to know I manage real estate - focus on residential small to large apartment buildings
• not strip malls, not giganic complexes - im a mid size company
• logo is black but i welcome color as u see fit
Nice to have
• maybe pictures
• my slogan - " we will manage your building like its our own "
• focus on professioanl, safe, trust worthy
• type style should be clear and readable - but im open to sugestions

```html
<!DOCTYPE html>
<html lang="en">
<head>
<meta charset="utf-8">
<title>RW Stewardship – Presentation Folder</title>
<link rel="stylesheet" href="https://fonts.googleapis.com/css2?family=Open+Sans:wght@400;600;700&display=swap">
<style>
  :root {
    --stage: #4b4b4b;
    --navy-deep: #070a2e;
    --navy: #14196b;
    --navy-glow: #2a34a8;
    --band: #050505;
    --rule: #d9d9d9;
    --white: #ffffff;
    --paper-light: #f4f4f4;
    --paper-mid: #dcdcdc;
    --ghost: #b9b9b9;
    --brick-1: #8a4a36;
    --brick-2: #b67a5a;
    --stone: #c9b58c;
    --sky: #6f8fb8;
  }
  * { margin: 0; padding: 0; box-sizing: border-box; }
  html, body { width: 800px; height: 1200px; overflow: hidden; }
  body {
    background: var(--stage);
    font-family: "Open Sans", Arial, sans-serif;
    position: relative;
  }

  .spread {
    position: absolute;
    left: 40px;
    width: 720px;
    height: 480px;
    display: flex;
    box-shadow: 0 14px 30px rgba(0,0,0,.45);
  }
  .spread--outside { top: 60px; }
  .spread--inside { top: 660px; }

  .panel { position: relative; width: 360px; height: 100%; overflow: hidden; }

  /* Outside */
  .spread--outside {
    background:
      radial-gradient(ellipse 300px 220px at 360px 200px, rgba(42,52,168,.55), transparent 70%),
      linear-gradient(160deg, var(--navy) 0%, var(--navy-deep) 70%);
  }
  .band {
    position: absolute; left: 0; right: 0; top: 196px; height: 112px;
    background: var(--band);
    border-top: 3px solid var(--rule);
    border-bottom: 3px solid var(--rule);
    box-shadow: 0 -6px 0 -3px var(--band), 0 6px 0 -3px var(--band);
  }
  .photo-row { position: absolute; display: flex; gap: 10px; }
  .photo {
    width: 66px; height: 66px;
    border: 4px solid var(--white);
    border-radius: 9px;
    background: linear-gradient(180deg, var(--sky) 0%, var(--sky) 22%, var(--brick-2) 23%, var(--brick-1) 100%);
  }
  .photo--stone { background: linear-gradient(180deg, var(--sky) 0%, var(--sky) 18%, var(--stone) 19%, #a48f68 100%); }
  .photo--red { background: linear-gradient(180deg, var(--sky) 0%, var(--sky) 26%, #a8503f 27%, #6e2f26 100%); }

  .back .photo-row { left: 30px; top: 218px; }
  .front .photo-row { left: 28px; top: 42px; }

  .slogan {
    color: var(--white);
    font-weight: 700;
    font-size: 13px;
    white-space: nowrap;
  }
  .back .slogan { position: absolute; left: 40px; top: 170px; }
  .front .slogan { position: absolute; left: 0; right: 0; top: 345px; text-align: center; }

  .brand-name {
    color: var(--white);
    font-weight: 700;
    letter-spacing: .04em;
    text-transform: uppercase;
    white-space: nowrap;
  }
  .front .brand-name {
    position: absolute; left: 0; right: 0; top: 236px;
    text-align: center; font-size: 24px;
  }

  .contact {
    position: absolute; left: 80px; top: 370px;
    color: var(--white); font-size: 9px; line-height: 1.55;
  }
  .contact .brand-name { font-size: 12px; margin-bottom: 6px; }
  .contact-line { display: flex; align-items: center; gap: 5px; }
  .contact-line svg { width: 9px; height: 9px; fill: var(--white); }
  .contact-phones { gap: 14px; }

  /* Inside */
  .spread--inside .panel {
    background: linear-gradient(135deg, var(--paper-light) 0%, var(--paper-mid) 100%);
  }
  .inside-left { border-right: 1px solid #c4c4c4; }
  .ghost-mark {
    position: absolute; left: 0; right: 0; top: 120px; text-align: center;
  }
  .ghost-mark .brand-name { color: var(--ghost); font-size: 26px; }
  .ghost-mark .slogan { color: var(--ghost); position: static; margin-top: 22px; }

  .pocket {
    position: absolute; left: 0; right: 0; bottom: 0; height: 150px;
    background: var(--band);
  }
  .inside-left .pocket { right: 4px; border-top-right-radius: 10px; }
  .inside-right .pocket { left: 4px; border-top-left-radius: 10px; }
  .pocket-brand { position: absolute; left: 0; right: 0; top: 40px; text-align: center; }
  .pocket-brand .brand-name { font-size: 18px; }
  .pocket-brand .slogan { position: static; margin-top: 14px; font-size: 12px; }

  .business-card {
    position: absolute; right: 28px; top: 22px;
    width: 156px; height: 84px;
    background: var(--white);
    border: 2px solid var(--white);
    outline: 1px solid #888;
    outline-offset: -4px;
    padding: 7px 8px;
    display: flex; flex-direction: column;
    color: #111; font-size: 4.6px; line-height: 1.35;
  }
  .card-top { display: flex; gap: 6px; flex: 1; }
  .card-brand {
    width: 48px; border-right: 1px solid #333;
    display: flex; align-items: center;
    font-weight: 700; font-size: 6px; text-transform: uppercase;
  }
  .card-name { font-size: 9px; font-weight: 700; line-height: 1.1; }
  .card-title { font-size: 4.6px; text-transform: uppercase; margin-bottom: 2px; }
  .card-slogan {
    border-top: 1px solid #333; padding-top: 2px;
    text-align: center; text-transform: uppercase; font-size: 4.4px;
  }
</style>
</head>
<body>

<section class="spread spread--outside" aria-label="Folder outside">
  <div class="band"></div>

  <div class="panel back">
    <p class="slogan">We will manage your building like it is our own</p>
    <div class="photo-row">
      <div class="photo photo--red" role="img" aria-label="Photo of a brick apartment building"></div>
      <div class="photo" role="img" aria-label="Photo of a corner apartment building"></div>
      <div class="photo photo--stone" role="img" aria-label="Photo of a mid-rise residential building"></div>
      <div class="photo photo--red" role="img" aria-label="Photo of a red brick apartment block"></div>
    </div>
    <div class="contact">
      <p class="brand-name">RW Stewardship</p>
      <p class="contact-line">
        <svg viewBox="0 0 10 10"><path d="M5 0a3.5 3.5 0 0 0-3.5 3.5C1.5 6 5 10 5 10s3.5-4 3.5-6.5A3.5 3.5 0 0 0 5 0zm0 5a1.4 1.4 0 1 1 0-2.8A1.4 1.4 0 0 1 5 5z"/></svg>
        22 Alder Court Suite 4, Yonkers, NY 10701
      </p>
      <p class="contact-line contact-phones">
        <span class="contact-line"><svg viewBox="0 0 10 10"><path d="M2 .5l2 2-1 1.3c.6 1.3 1.6 2.3 2.9 2.9L7.2 5.7l2.3 2L8.4 9.5C4.3 9.2.8 5.7.5 1.6z"/></svg>914-555-0182</span>
        <span class="contact-line"><svg viewBox="0 0 10 10"><rect x="2.5" y="0" width="5" height="10" rx="1"/></svg>917-555-0147</span>
      </p>
      <p class="contact-line">
        <svg viewBox="0 0 10 10"><path d="M0 2h10v6H0zM.6 2.4L5 5.6l4.4-3.2"/></svg>
        dreyes@rwstewardship.com
      </p>
    </div>
  </div>

  <div class="panel front">
    <div class="photo-row">
      <div class="photo" role="img" aria-label="Photo of brownstone townhouses"></div>
      <div class="photo photo--red" role="img" aria-label="Photo of a brick apartment building on a corner"></div>
      <div class="photo" role="img" aria-label="Photo of a residential building with street view"></div>
      <div class="photo photo--stone" role="img" aria-label="Photo of a tan stone apartment building"></div>
    </div>
    <p class="brand-name">RW Stewardship</p>
    <p class="slogan">We will manage your building like it is our own</p>
  </div>
</section>

<section class="spread spread--inside" aria-label="Folder inside">
  <div class="panel inside-left">
    <div class="pocket">
      <div class="pocket-brand">
        <p class="brand-name">RW Stewardship</p>
        <p class="slogan">We will manage your building like it is our own</p>
      </div>
    </div>
  </div>

  <div class="panel inside-right">
    <div class="ghost-mark">
      <p class="brand-name">RW Stewardship</p>
      <p class="slogan">We will manage your building like it is our own</p>
    </div>
    <div class="pocket">
      <div class="business-card">
        <div class="card-top">
          <div class="card-brand">RW Stewardship</div>
          <div class="card-details">
            <p class="card-name">Daniel Reyes</p>
            <p class="card-title">Building Manager</p>
            <p>office 914-555-0182</p>
            <p>email dreyes@rwstewardship.com</p>
            <p>cell 917-555-0147</p>
            <p>22 Alder Court, Suite 4, Yonkers NY</p>
          </div>
        </div>
        <p class="card-slogan">We will manage your building like it is our own</p>
      </div>
    </div>
  </div>
</section>

</body>
</html>
```